Abu Kemo's Chimichurri Sauce

We need a label for a 10 ounce jar of a pesto type sauce using the argentine flag for color cues. the label would wrap around the jar. There would be room for how to use the sauce. About 20.5 cm length and 5 cm height. There would be a faded image of a man on a bycycle where the back story is told in 48 words with small signature and underneath a website there has to be room for the UPC code and also the ingrediant panel.

thhe back story over spanish looking boy with bike ideally near city scape but looking like it could be from 50's.

Young Kemo would bycycle from store to resataurant to grocer selling his Mother's jarred Chimichurri sauce. Each day the shop owners would say "Where is Abukemo?" The sauce handed down over generations is an Argentine national secret that makes every piece of meat, chicken, pasta, dip or eggs pop with excitement and bold taste. Sealed Fresh with Care....(signature) Abu Kemo

The name of the product id Abu Kemo's Chimichurri Sealed Fresh with Care
the label on back would be a box called Nutrition Facts. Serving Size 1 Tblsn (3g), Servings About 50 ;Amount Calories??/;Total Fat??/;Chol ??/Sodium???Total Carbs???Protein ????Vitamin A??Vitamin C;Calcium????????????????

Then Underneath that: Ingredients : Vegetable Oil,Vinegar,Parsley Garlic Chilli Fales,Pepper, Salt

The website: abukemos-sample.com
Abukemos Foods LLC Youngstown, Ohio 44505

Some place else bold NON GMO NO PRESERVATIVES GLUEN FREE CHOLESTERAL FREE VEGAN PLEASE RECYCLE

Target Market(s)

Shoppers at high end grocery stores and farmer markets

Industry/Entity Type

Food Production

Colors
fbed22
ffffff
0292cd

Requirements
Must have
• bright argentine colors and references
Nice to have
• The argentine flag is fun and colorful. Look at that. We want to make a back story of a young Abukemo bycycling through Buenes Aries in th e40's or 50's selling his mother's homemade sauce. This stuff tastes fantastic.

```html
<!DOCTYPE html>
<html lang="en">
<head>
<meta charset="utf-8">
<title>Abu Kemo's Chimichurri – Jar Label</title>
<link href="https://fonts.googleapis.com/css2?family=Crimson+Text:wght@400;700&family=Dancing+Script:wght@500&family=Mrs+Saint+Delafield&family=Open+Sans:wght@400;600&family=Roboto+Slab:wght@400;500&display=swap" rel="stylesheet">
<style>
  :root {
    --bg: #e4e4e4;
    --label-yellow: #f6cf14;
    --ink: #3a3320;
    --black: #111111;
    --white: #ffffff;
    --sky-blue: #5ea3d8;
    --orange: #e8821f;
    --deep-orange: #d2561d;
    --green-soft: #9bc24a;
    --badge-dark: #2b2a26;
    --badge-gold: #c9a227;
    --heart-red: #c9442a;
    --sun-cream: #f7efcf;
    --field-light: #f3d97a;
  }
  * { margin: 0; padding: 0; box-sizing: border-box; }
  html, body { width: 1200px; height: 800px; overflow: hidden; background: var(--bg); }
  .canvas { position: relative; width: 1200px; height: 800px; }

  .label {
    position: absolute; top: 258px; width: 318px; height: 322px;
    background: var(--label-yellow);
    box-shadow: 0 8px 22px rgba(0,0,0,.12);
  }
  .label--back { left: 190px; }
  .label--front { left: 668px; }

  /* ---------- back panel ---------- */
  .story-art {
    position: absolute; left: 80px; top: 24px; width: 68px; height: 58px;
    border-radius: 6px; background: linear-gradient(180deg, #f2c814, #dcb316);
  }
  .story-text {
    position: absolute; left: 18px; top: 100px; width: 224px;
    font-family: "Crimson Text", serif; font-size: 11px; line-height: 12.6px;
    color: var(--ink); text-align: justify;
  }
  .signature {
    position: absolute; right: 76px; top: 204px; text-align: right;
    font-family: "Mrs Saint Delafield", cursive; font-size: 17px; line-height: 17px;
    color: var(--ink);
  }
  .upc-space {
    position: absolute; left: 22px; top: 234px; width: 121px; height: 60px;
    background: var(--black); color: var(--white);
    font-family: "Open Sans", sans-serif; font-size: 25px; line-height: 60px;
    text-align: center; letter-spacing: -.5px;
  }
  .maker {
    position: absolute; left: 22px; top: 298px; width: 124px;
    font-family: "Open Sans", sans-serif; font-size: 6.5px; line-height: 8px;
    color: var(--ink);
  }
  .maker-site { font-weight: 600; }

  .nutrition {
    position: absolute; left: 156px; top: 240px; width: 146px; height: 76px;
    border: 1px solid var(--ink); padding: 3px 4px;
    font-family: "Open Sans", sans-serif; color: var(--ink);
  }
  .nutrition-title {
    font-family: "Crimson Text", serif; font-weight: 700; font-size: 10px; line-height: 10px;
    border-bottom: 1px solid var(--ink); padding-bottom: 2px;
  }
  .nutrition-serving { font-size: 5.5px; line-height: 7px; border-bottom: 2px solid var(--ink); }
  .nutrition-rows { display: grid; grid-template-columns: 1fr 1fr; column-gap: 6px; font-size: 5.5px; line-height: 6.6px; margin-top: 1px; }
  .nutrition-rows span { border-bottom: .5px solid rgba(58,51,32,.5); }
  .ingredients { font-size: 5.5px; line-height: 6.6px; margin-top: 2px; }
  .ingredients b { font-weight: 600; }

  /* ---------- front panel ---------- */
  .organic {
    position: absolute; left: 30px; top: 30px; transform: rotate(-18deg);
    font-family: "Dancing Script", cursive; font-size: 34px; line-height: 40px; color: var(--sky-blue);
  }
  .organic-ribbon {
    position: absolute; left: 98px; top: 48px; width: 84px; height: 15px;
    transform: rotate(-20deg); background: var(--sky-blue);
    font-family: "Crimson Text", serif; font-size: 9.5px; letter-spacing: 1px;
    color: var(--white); text-align: center; line-height: 15px;
  }
  .badge { position: absolute; top: 24px; width: 42px; height: 42px; border-radius: 50%; }
  .badge--dark { left: 222px; background: var(--badge-dark); border: 3px solid var(--badge-gold); }
  .badge--green { left: 266px; background: var(--green-soft); border: 2px solid var(--white); }

  .farm-scene {
    position: absolute; left: 80px; top: 62px; width: 170px; height: 170px;
    border-radius: 50%; border: 3px solid var(--orange);
    background: linear-gradient(180deg, var(--sun-cream) 0 44%, var(--green-soft) 44% 58%, var(--field-light) 58% 100%);
  }
  .name-banner {
    position: absolute; left: 16px; top: 196px; width: 294px; height: 34px;
    background: var(--sky-blue); transform: rotate(-1.5deg);
    clip-path: polygon(0 0, 100% 0, 96% 50%, 100% 100%, 0 100%, 4% 50%);
    font-family: "Roboto Slab", serif; font-weight: 500; font-size: 18px;
    color: var(--orange); text-align: center; line-height: 34px; white-space: nowrap;
  }
  .claim-icon { position: absolute; }
  .claim-icon--heart { left: 8px; top: 248px; }
  .heart-text {
    position: absolute; left: 12px; top: 262px; width: 30px;
    font-family: "Open Sans", sans-serif; font-size: 4px; line-height: 5px;
    color: var(--white); text-align: center;
  }
  .claim-icon--wheat { left: 56px; top: 254px; }
  .claim-icon--pumpkin { left: 132px; top: 252px; }
  .claim {
    position: absolute; font-family: "Crimson Text", serif; font-size: 10px; line-height: 10px;
    color: var(--ink); white-space: nowrap;
  }
  .claim--gmo { left: 56px; top: 292px; }
  .claim--pres { left: 108px; top: 296px; }
  .net-weight {
    position: absolute; left: 250px; top: 266px;
    font-family: "Roboto Slab", serif; font-size: 21px; line-height: 24px; color: var(--deep-orange);
  }
</style>
</head>
<body>
<main class="canvas">

  <section class="label label--back">
    <div class="story-art" role="img" aria-label="Faded sketch of a young man riding a bicycle"></div>
    <p class="story-text">Young Kemo would bycycle from store to resataurant to grocer selling his Mother's jarred Chimichurri sauce. Each day the shop owners would say "Where is Abukemo?" The sauce handed down over generations is an Argentine national secret that makes every piece of meat, chicken, pasta, dip or eggs pop with excitement and bold taste.</p>
    <p class="signature">Sealed Fresh with Care<br>Abu Kemo</p>

    <div class="upc-space">BAR CODE</div>
    <p class="maker"><span class="maker-site">abukemos-sample.com</span><br>Abukemos Foods LLC Youngstown, Ohio 44505</p>

    <div class="nutrition">
      <p class="nutrition-title">Nutrition Facts</p>
      <p class="nutrition-serving">Serving Size 1 Tbsp (3g) · Servings About 50</p>
      <div class="nutrition-rows">
        <span>Calories ??</span><span>Total Fat ??</span>
        <span>Cholesterol ??</span><span>Sodium ??</span>
        <span>Total Carbs ??</span><span>Protein ??</span>
        <span>Vitamin A ??</span><span>Vitamin C ??</span>
      </div>
      <p class="ingredients"><b>Ingredients:</b> Vegetable Oil, Vinegar, Parsley, Garlic, Chilli Flakes, Pepper, Salt</p>
    </div>
  </section>

  <section class="label label--front">
    <div class="organic">Organic</div>
    <div class="organic-ribbon">All Natural</div>
    <div class="badge badge--dark" aria-hidden="true"></div>
    <div class="badge badge--green" aria-hidden="true"></div>

    <div class="farm-scene" role="img" aria-label="Farm scene with a barn, sun, green hills and striped fields"></div>

    <h1 class="name-banner">ABU KEMO'S CHIMICHURRI</h1>

    <svg class="claim-icon claim-icon--heart" width="46" height="44" viewBox="0 0 46 44" aria-hidden="true">
      <path d="M23 43 C8 32 1 23 1 13 C1 6 7 1 13 1 C18 1 21 4 23 8 C25 4 28 1 33 1 C39 1 45 6 45 13 C45 23 38 32 23 43Z" fill="var(--heart-red)"/>
    </svg>
    <span class="heart-text">NO CHOLESTEROL</span>

    <svg class="claim-icon claim-icon--wheat" width="38" height="34" viewBox="0 0 40 36" aria-hidden="true">
      <g stroke="var(--green-soft)" stroke-width="2" fill="none">
        <path d="M8 36V8M20 36V2M32 36V8"/>
        <path d="M8 14l-5-4M8 14l5-4M8 22l-5-4M8 22l5-4M20 10l-5-4M20 10l5-4M20 18l-5-4M20 18l5-4M20 26l-5-4M20 26l5-4M32 14l-5-4M32 14l5-4M32 22l-5-4M32 22l5-4"/>
      </g>
    </svg>

    <svg class="claim-icon claim-icon--pumpkin" width="40" height="40" viewBox="0 0 40 40" aria-hidden="true">
      <ellipse cx="20" cy="23" rx="18" ry="16" fill="var(--orange)"/>
      <path d="M20 8v-6" stroke="#6b8f2a" stroke-width="3"/>
    </svg>

    <span class="claim claim--gmo">NON GMO</span>
    <span class="claim claim--pres">NO PRESERVATIVES</span>
    <span class="net-weight">10oz</span>
  </section>

</main>
</body>
</html>
```